Brightoakrx website

We are a weight loss clinic and we need a website built. please look at these websites for content and style. Just need like 5 pages see samples. AI files of logo are not avail yet so use sample for place set

https://slimshiftstudio.example/
qorvatherapy.example
https://pinecrestclinicalbodybalance.example/
https://yourslimmingcorner.example/
https://krvskincare.example/treatments/weight-loss-injections/

Target Market(s)

Women

Industry/Entity Type

weight loss

Coding

Coded - Design and coding required

Number of Pages Required

5+ page

Requirements
Nice to have
• please make look like a medspa website

```html
<!DOCTYPE html>
<html lang="en">
<head>
<meta charset="utf-8">
<title>Brightoakrx</title>
<link rel="stylesheet" href="https://fonts.googleapis.com/css2?family=Marcellus&family=Mulish:wght@400;600&display=swap">
<style>
:root{
  --green-dark:#1d6a50;
  --green-deep:#1a5c45;
  --green-leaf:#2a8a66;
  --green-soft:#5fb590;
  --mint:#cfe9dc;
  --paper:#f2f4f3;
  --white:#ffffff;
  --gold:#d9a23a;
  --text-green:#1f5f47;
  --quote-gold:#f0d9a8;
}
*{margin:0;padding:0;box-sizing:border-box}
html,body{width:1200px;height:3926px;overflow:hidden}
body{position:relative;background:var(--paper);font-family:"Mulish",sans-serif;color:var(--text-green)}
.abs{position:absolute}
.serif{font-family:"Marcellus",serif}

.site-nav{left:0;top:0;width:1200px;height:50px;background:var(--white);z-index:2}
.nav-link{top:18px;font-size:12px;letter-spacing:.3px;color:#1b3e33}
.nav-link.accent{color:var(--green-leaf)}
.nav-link.book{color:var(--gold);top:22px}
.brand{left:510px;top:10px;display:flex;align-items:center;gap:6px;font-family:"Marcellus",serif;font-size:20px;color:var(--green-leaf)}
.brand-dot{width:22px;height:22px;border-radius:50%;background:var(--green-soft)}

.hero{left:0;top:50px;width:1200px;height:522px;background:linear-gradient(180deg,#c9c6bd 0%,#a9a69f 45%,#6f6d69 100%)}
.hero-title{left:300px;top:196px;width:600px;text-align:center;font-size:42px;line-height:50px;color:var(--white)}

.staff{left:0;top:572px;width:1200px;height:1640px;background:linear-gradient(180deg,#1f7a58 0%,#1e6e52 45%,var(--green-dark) 100%)}
.staff-title{left:0;top:82px;width:1200px;text-align:center;font-size:36px;color:var(--white)}
.staff-list{left:159px;top:180px;width:884px;background:var(--white)}
.staff-row{display:flex;height:453px}
.staff-photo{width:442px;height:453px}
.staff-body{padding:58px 52px 0 44px;width:442px}
.staff-name{font-family:"Marcellus",serif;font-size:23px;margin-bottom:14px}
.staff-body p{font-size:12.5px;line-height:21px;margin-bottom:12px}
.social{display:flex;gap:10px;margin-top:6px}
.social span{width:8px;height:8px;border-radius:50%;background:var(--gold)}

.leaf-band{left:0;top:2212px;width:1200px;height:304px;background:linear-gradient(180deg,#2d8763 0%,#4fa57f 55%,rgba(242,244,243,0) 100%)}

.opinions-title{left:0;top:2608px;width:1200px;text-align:center;font-size:36px;color:var(--green-deep)}
.review{width:390px}
.avatar{width:84px;height:84px;border-radius:50%}
.quote-mark{position:absolute;left:0;top:96px;font-family:"Marcellus",serif;font-size:60px;line-height:60px;color:var(--quote-gold)}
.review p{margin:42px 0 0 18px;font-size:13px;line-height:23px;color:#2a5b49}
.reviewer{margin:30px 0 0 18px;font-size:12px;color:var(--gold);display:flex;align-items:center;gap:6px}

.bottom-fade{left:0;top:3300px;width:1200px;height:230px;background:linear-gradient(180deg,rgba(242,244,243,0) 0%,var(--mint) 100%)}
.footer{left:0;top:3510px;width:1200px;height:416px}
.footer-text{left:0;top:3728px;width:1200px;text-align:center;font-family:"Marcellus",serif;color:var(--white);font-size:14px;line-height:24px}
</style>
</head>
<body>

<header class="abs site-nav">
  <span class="abs nav-link" style="left:221px">HOME</span>
  <span class="abs nav-link" style="left:294px">SERVICES</span>
  <span class="abs nav-link" style="left:393px">PRICING</span>
  <div class="abs brand"><span class="brand-dot"></span>Brightoakrx</div>
  <span class="abs nav-link accent" style="left:736px">ABOUT</span>
  <span class="abs nav-link" style="left:816px">CONTACT</span>
  <span class="abs nav-link book" style="left:926px">BOOK ONLINE</span>
</header>

<section class="abs hero" role="img" aria-label="Smiling woman in sportswear sitting on a seaside path"></section>
<h1 class="abs hero-title serif" style="top:196px">The natural way of gaining perfect body &amp; health</h1>

<section class="abs staff" role="img" aria-label="Background of large tropical leaves">
  <h2 class="abs staff-title serif">Our staff is always here to help</h2>
  <div class="abs staff-list">
    <article class="staff-row">
      <div class="staff-photo" role="img" aria-label="Portrait of a staff member with curly hair" style="background:linear-gradient(135deg,#b8c6c9,#8a6a4f)"></div>
      <div class="staff-body">
        <h3 class="staff-name">Talia Brenner</h3>
        <p>Mauris rhoncus orci in imperdiet placerat. Vestibulum euismod nisl suscipit ligula volutpat, a feugiat urna maximus. Cras massa nibh, tincidunt ut eros a, vulputate consequat odio. Vestibulum vehicula tempor nulla, sed hendrerit urna interdum in.</p>
        <p>Morbi vestibulum id tellus commodo mattis. Aliquam erat volutpat. Aenean accumsan id mi nec semper. Sed ultrices nisl velit, eu ornare est ullamcorper a. Nunc quis nibh magna. Proin risus erat, fringilla vel purus sit amet, mattis porta enim. Duis fermentum faucibus est, sed vehicula velit sodales vitae. Mauris mollis lobortis turpis, eget accumsan ante aliquam quis.</p>
        <div class="social"><span></span><span></span><span></span></div>
      </div>
    </article>
    <article class="staff-row">
      <div class="staff-photo" role="img" aria-label="Portrait of a staff member with long dark hair" style="background:linear-gradient(135deg,#e4dcd8,#a88a7a)"></div>
      <div class="staff-body">
        <h3 class="staff-name">Talia Brenner</h3>
        <p>Mauris rhoncus orci in imperdiet placerat. Vestibulum euismod nisl suscipit ligula volutpat, a feugiat urna maximus. Cras massa nibh, tincidunt ut eros a, vulputate consequat odio. Vestibulum vehicula tempor nulla, sed hendrerit urna interdum in.</p>
        <p>Morbi vestibulum id tellus commodo mattis. Aliquam erat volutpat. Aenean accumsan id mi nec semper. Sed ultrices nisl velit, eu ornare est ullamcorper a. Nunc quis nibh magna. Proin risus erat, fringilla vel purus sit amet, mattis porta enim. Duis fermentum faucibus est, sed vehicula velit sodales vitae. Mauris mollis lobortis turpis, eget accumsan ante aliquam quis.</p>
        <div class="social"><span></span><span></span><span></span></div>
      </div>
    </article>
    <article class="staff-row">
      <div class="staff-photo" role="img" aria-label="Portrait of a staff member with blonde hair outdoors" style="background:linear-gradient(160deg,#5f8a4a,#d9c08a 55%,#e8c63a)"></div>
      <div class="staff-body">
        <h3 class="staff-name">Talia Brenner</h3>
        <p>Mauris rhoncus orci in imperdiet placerat. Vestibulum euismod nisl suscipit ligula volutpat, a feugiat urna maximus. Cras massa nibh, tincidunt ut eros a, vulputate consequat odio. Vestibulum vehicula tempor nulla, sed hendrerit urna interdum in.</p>
        <p>Morbi vestibulum id tellus commodo mattis. Aliquam erat volutpat. Aenean accumsan id mi nec semper. Sed ultrices nisl velit, eu ornare est ullamcorper a. Nunc quis nibh magna. Proin risus erat, fringilla vel purus sit amet, mattis porta enim. Duis fermentum faucibus est, sed vehicula velit sodales vitae. Mauris mollis lobortis turpis, eget accumsan ante aliquam quis.</p>
        <div class="social"><span></span><span></span><span></span></div>
      </div>
    </article>
  </div>
</section>

<div class="abs leaf-band" role="img" aria-label="Border of hanging tropical leaves"></div>

<h2 class="abs opinions-title serif">Opinions about us</h2>

<article class="abs review" style="left:188px;top:2740px">
  <div class="avatar" role="img" aria-label="Client avatar" style="background:linear-gradient(135deg,#c9b8a6,#6b5443)"></div>
  <span class="quote-mark">”</span>
  <p>Vitae adipiscing turpis. Aenean ligula nibh, molestie id viverra a, dapibus at dolor. In iaculis viverra neque, ac eleifend ante lobortis id. In in leo ultrices posuere ante viverra ipsum ...</p>
  <div class="reviewer"><svg width="11" height="11" viewBox="0 0 11 11"><circle cx="5.5" cy="3" r="2.6" fill="#d9a23a"/><path d="M0.5 11c0-3 2.2-4.6 5-4.6s5 1.6 5 4.6z" fill="#d9a23a"/></svg>Nora Elwood</div>
</article>
<article class="abs review" style="left:630px;top:2740px">
  <div class="avatar" role="img" aria-label="Client avatar" style="background:linear-gradient(135deg,#8a5a4a,#2e2420)"></div>
  <span class="quote-mark">”</span>
  <p>Vitae adipiscing turpis. Aenean ligula nibh, molestie id viverra a, dapibus at dolor. In iaculis viverra neque, ac eleifend ante lobortis id. In in leo ultrices posuere ante viverra ipsum ...</p>
  <div class="reviewer"><svg width="11" height="11" viewBox="0 0 11 11"><circle cx="5.5" cy="3" r="2.6" fill="#d9a23a"/><path d="M0.5 11c0-3 2.2-4.6 5-4.6s5 1.6 5 4.6z" fill="#d9a23a"/></svg>Nora Elwood</div>
</article>
<article class="abs review" style="left:188px;top:3083px">
  <div class="avatar" role="img" aria-label="Client avatar" style="background:linear-gradient(135deg,#c58a5a,#3a2a30)"></div>
  <span class="quote-mark">”</span>
  <p>Vitae adipiscing turpis. Aenean ligula nibh, molestie id viverra a, dapibus at dolor. In iaculis viverra neque, ac eleifend ante lobortis id. In in leo ultrices posuere ante viverra ipsum ...</p>
  <div class="reviewer"><svg width="11" height="11" viewBox="0 0 11 11"><circle cx="5.5" cy="3" r="2.6" fill="#d9a23a"/><path d="M0.5 11c0-3 2.2-4.6 5-4.6s5 1.6 5 4.6z" fill="#d9a23a"/></svg>Nora Elwood</div>
</article>
<article class="abs review" style="left:630px;top:3083px">
  <div class="avatar" role="img" aria-label="Client avatar" style="background:linear-gradient(135deg,#c58a5a,#3a2a30)"></div>
  <span class="quote-mark">”</span>
  <p>Vitae adipiscing turpis. Aenean ligula nibh, molestie id viverra a, dapibus at dolor. In iaculis viverra neque, ac eleifend ante lobortis id. In in leo ultrices posuere ante viverra ipsum ...</p>
  <div class="reviewer"><svg width="11" height="11" viewBox="0 0 11 11"><circle cx="5.5" cy="3" r="2.6" fill="#d9a23a"/><path d="M0.5 11c0-3 2.2-4.6 5-4.6s5 1.6 5 4.6z" fill="#d9a23a"/></svg>Nora Elwood</div>
</article>

<div class="abs bottom-fade"></div>

<svg class="abs footer" viewBox="0 0 1200 416" aria-hidden="true">
  <defs>
    <linearGradient id="footer-fill" x1="0" y1="0" x2="0" y2="1">
      <stop offset="0" stop-color="#1d6a50"/>
      <stop offset="1" stop-color="#1a5c45"/>
    </linearGradient>
  </defs>
  <path d="M0 16 H540 C580 16 598 0 600 -10 C602 0 620 16 660 16 H1200 V416 H0 Z" fill="url(#footer-fill)"/>
  <path d="M1010 386 l7 -6 l7 6" fill="none" stroke="#5fb590" stroke-width="1.5"/>
</svg>
<div class="abs footer-text">
  Nullam viverra consectetuer quisque cursus et, porttitor risus.<br>
  <span style="font-size:13px">+61 (0) 3555 0100 &nbsp;hello@brightoakrx.example</span>
</div>

</body>
</html>
```